Webdesign für KOR GmbH
Zielgruppe
KOR GmbH - Spezialist für Anlasser und Lichtmaschinen
Gegründet 1992 ist KOR nunmehr ein deutschlandweit agierendes Unternehmen mit 13 Mitarbeitern. Der Fokus unserer Arbeit liegt dabei auf der professionellen Regenerierung von Anlassern und Lichtmaschinen. Die strikte Arbeit nach Herstellerstandards und der hohe Anspruch an Qualität und Qualitätssicherung wurde durch die Einführung der ISO Zertifizierung 9001 untermauert.
Der Vertrieb von:
Anlassern
Lichtmaschinen
Turboladern
Klimakompressoren
Verdampfern / Kondensatoren
Batterien
namenhafter Hersteller ergänzt das Portfolio. Die Spezialisierung auf diese Produktgruppen ermöglicht dabei ein hohes Maß an Verfügbarkeit und marktgerechte Preise.
- Modern
- Klares und übersichtliches Desgin
- Nicht zu verspielt
- Informativ
- Leichte Navigation
- Das Design der alten Webseite soll NICHT kopiert werden
- Die Farben des Logos sollen sich wiederfinden

```html
<!DOCTYPE html>
<html lang="de">
<head>
<meta charset="utf-8">
<title>KOR GmbH – Anlasser und Lichtmaschinen</title>
<link href="https://fonts.googleapis.com/css2?family=Inter:wght@400;500;600;700&display=swap" rel="stylesheet">
<style>
:root{
  --navy:#0f172a;
  --navy-2:#111c33;
  --green:#15803d;
  --green-bright:#34d399;
  --green-soft:#ecfdf5;
  --text:#0f172a;
  --muted:#64748b;
  --line:#e2e8f0;
  --light:#f8fafc;
  --white:#ffffff;
}
*{box-sizing:border-box;margin:0;padding:0}
html,body{width:1200px;height:3671px;overflow:hidden}
body{font-family:"Inter",sans-serif;color:var(--text);background:var(--white);font-size:14px}
.wrap{width:1032px;margin:0 auto;position:relative}
svg{display:block}

/* nav */
.nav{height:54px;background:#eef0f1;border-bottom:1px solid #d7dbe0;display:flex;align-items:center}
.nav .wrap{display:flex;align-items:center;justify-content:space-between}
.brand{display:flex;align-items:center;gap:8px;color:var(--green);font-weight:700;font-size:15px}
.brand-dot{width:22px;height:22px;border-radius:50%;border:2px solid var(--green)}
.nav-links{display:flex;gap:26px;font-size:12px;color:#475569;margin-left:70px}
.btn-contact{background:var(--green);color:#fff;font-size:11px;font-weight:600;padding:9px 14px;border-radius:4px;border:2px solid #86efac}

/* hero */
.hero{height:698px;position:relative;color:#fff;overflow:hidden}
.hero-photo{position:absolute;inset:0;background:radial-gradient(ellipse 45% 60% at 68% 42%,#3a4450 0%,#1c2530 45%,transparent 75%),linear-gradient(100deg,#0b1424 0%,#0d1b2a 40%,#12352f 80%,#0f4a37 100%)}
.hero .wrap{padding-top:107px}
.badge{display:inline-flex;align-items:center;gap:6px;border:1px solid #16a34a;color:#4ade80;background:rgba(22,163,74,.12);border-radius:20px;font-size:10px;font-weight:600;padding:4px 12px;letter-spacing:.04em}
.hero h1{font-size:50px;line-height:1.0;font-weight:600;letter-spacing:-.02em;margin-top:20px}
.hero h1 span{color:var(--green-bright)}
.hero p{font-size:15px;line-height:1.65;color:#d5dbe3;width:430px;margin-top:28px}
.hero-btns{display:flex;gap:14px;margin-top:28px}
.btn{font-size:12px;font-weight:600;padding:10px 20px;border-radius:4px;display:inline-flex;align-items:center;gap:7px}
.btn-green{background:var(--green);color:#fff}
.btn-dark{background:rgba(255,255,255,.06);border:1px solid #4b5563;color:#fff}
.hero-divider{width:560px;height:1px;background:rgba(255,255,255,.15);margin-top:40px}
.stats{display:flex;margin-top:30px}
.stat{width:127px}
.stat:nth-child(2){width:131px}
.stat b{font-size:20px;font-weight:600;display:block}
.stat small{font-size:9.5px;letter-spacing:.05em;color:#94a3b8;font-weight:500}

/* categories */
.cats{height:732px;padding-top:84px}
.cats-head{display:flex;justify-content:space-between;align-items:flex-end}
.cats h2{font-size:24px;font-weight:600;letter-spacing:-.01em}
.cats-head p{font-size:13px;color:var(--muted);line-height:1.55;width:420px;margin-top:12px}
.link-green{color:var(--green);font-size:12px;font-weight:600;display:flex;align-items:center;gap:5px}
.grid{display:grid;grid-template-columns:repeat(3,331px);gap:20px 20px;margin-top:42px}
.card{border:1px solid var(--line);border-radius:8px;padding:24px 34px 24px 20px;height:249px}
.grid .short{height:178px}
.icon{width:38px;height:38px;border-radius:6px;background:var(--green-soft);display:flex;align-items:center;justify-content:center;color:var(--green)}
.card h3{font-size:15px;font-weight:600;margin-top:26px}
.card p{font-size:11.5px;color:var(--muted);line-height:1.5;margin-top:11px}
.ticks{list-style:none;margin-top:12px}
.ticks li{font-size:10px;color:#475569;display:flex;align-items:center;gap:6px;margin-bottom:8px}

/* service */
.service{height:584px;background:var(--navy-2);color:#fff;overflow:hidden}
.service .wrap{display:flex;padding-top:88px}
.service-img{position:relative;width:543px;height:410px}
.service-frame{position:absolute;left:-18px;top:18px;width:510px;height:355px;background:#173d33;border-radius:8px;transform:rotate(-2deg)}
.service-photo{position:absolute;left:0;top:35px;width:489px;height:333px;border-radius:6px;background:linear-gradient(110deg,#5b6a6f 0%,#a26a3b 25%,#cfd3d4 55%,#6e8aa8 80%,#2f5b9a 100%)}
.guarantee{position:absolute;left:294px;top:287px;width:215px;height:80px;background:#fff;border-radius:6px;color:var(--text);display:flex;align-items:center;gap:12px;padding:0 18px;box-shadow:0 10px 24px rgba(0,0,0,.25)}
.g-ic{width:32px;height:32px;border-radius:50%;background:var(--green-soft);display:flex;align-items:center;justify-content:center;color:var(--green)}
.guarantee b{font-size:12px;display:block}
.guarantee small{font-size:9.5px;color:var(--muted)}
.service-text{width:489px;position:relative}
.service-deco{position:absolute;right:-30px;top:-20px;width:280px;height:280px;border-radius:50%;border:44px solid rgba(148,163,184,.07)}
.eyebrow{display:flex;align-items:center;gap:8px;font-size:11px;font-weight:500;letter-spacing:.06em;color:#4ade80;position:relative}
.eyebrow:before{content:"";width:24px;height:1px;background:currentColor}
.service h2{font-size:30px;font-weight:600;line-height:1.15;letter-spacing:-.01em;margin-top:14px;position:relative}
.service p.lead{font-size:13px;color:#94a3b8;line-height:1.7;margin-top:22px;position:relative}
.steps{list-style:none;margin-top:22px;position:relative}
.steps li{display:flex;gap:14px;margin-bottom:18px}
.num{width:20px;height:20px;border-radius:50%;background:#1e293b;color:#94a3b8;font-size:9px;display:flex;align-items:center;justify-content:center;flex:none;margin-top:2px}
.steps b{font-size:13px;font-weight:500;display:block}
.steps span{font-size:11px;color:#94a3b8;margin-top:5px;display:block}
.service .link-green{color:#4ade80;font-size:13px;margin-top:8px;position:relative}

/* quality */
.quality{height:561px}
.quality .wrap{display:flex;justify-content:space-between;padding-top:84px}
.q-left{width:496px}
.quality .eyebrow{color:var(--green)}
.quality h2{font-size:26px;font-weight:600;line-height:1.2;margin-top:16px}
.quality p.lead{font-size:13px;color:var(--muted);line-height:1.7;margin-top:18px}
.q-photos{display:flex;gap:15px;margin-top:32px}
.q-photo{width:240px;height:179px;border-radius:4px}
.q-photo.one{background:linear-gradient(135deg,#eceae3 0%,#2f8f6a 45%,#3a3a38 75%,#1f2b25 100%)}
.q-photo.two{background:linear-gradient(135deg,#1b5a3f 0%,#20613f 50%,#163f2c 100%)}
.q-card{width:496px;height:333px;margin-top:30px;background:var(--light);border:1px solid var(--line);border-radius:12px;padding:40px 40px;position:relative;overflow:hidden}
.q-card h3{font-size:16px;font-weight:600}
.q-shield{position:absolute;right:20px;top:10px;color:#e5e9ee}
.q-item{display:flex;gap:16px;margin-top:24px;position:relative}
.q-ic{width:30px;height:30px;border-radius:50%;background:#fff;border:1px solid var(--line);display:flex;align-items:center;justify-content:center;color:var(--green);flex:none}
.q-item b{font-size:13px;font-weight:500;display:block}
.q-item span{font-size:11px;color:var(--muted);line-height:1.5;display:block;margin-top:2px}

/* contact */
.contact{height:727px;background:var(--light);padding-top:80px}
.contact h2{font-size:24px;font-weight:600;text-align:center}
.contact .sub{font-size:13px;color:var(--muted);text-align:center;line-height:1.6;width:600px;margin:14px auto 0}
.contact-grid{display:flex;gap:26px;width:818px;margin:44px auto 0}
.c-info{width:255px;display:flex;flex-direction:column;gap:14px}
.c-card{background:#fff;border:1px solid var(--line);border-radius:8px;padding:20px 20px;height:148px}
.c-card:nth-child(2),.c-card:nth-child(3){height:133px}
.c-card .ic{color:var(--green)}
.c-card b{font-size:13px;font-weight:600;display:block;margin-top:14px}
.c-card span{font-size:11px;color:var(--muted);line-height:1.55;display:block;margin-top:5px}
.form{width:537px;height:440px;background:#fff;border:1px solid var(--line);border-radius:8px;padding:28px 27px}
.row{display:flex;gap:20px}
.field{flex:1;margin-bottom:24px}
.field label{font-size:10px;font-weight:500;color:#334155;display:block;margin-bottom:10px}
.input{height:30px;border:1px solid var(--line);background:var(--light);border-radius:3px}
.textarea{height:82px}
.consent{display:flex;align-items:center;gap:8px;font-size:9.5px;color:var(--muted);margin-top:-4px}
.consent i{width:12px;height:12px;border:1px solid #94a3b8;border-radius:2px;display:block}
.consent u{color:#334155}
.btn-send{display:inline-block;background:var(--green);color:#fff;font-size:12px;font-weight:600;padding:11px 27px;border-radius:3px;margin-top:22px}

/* footer */
.footer{height:315px;background:var(--navy);color:#94a3b8;padding-top:56px}
.f-top{display:flex}
.f-brand{width:423px}
.f-brand .brand{color:#fff;font-size:12px}
.f-brand .brand-dot{border-color:#fff;width:16px;height:16px}
.f-brand p{font-size:11.5px;line-height:1.6;margin-top:26px;width:340px}
.socials{display:flex;gap:14px;margin-top:18px}
.socials i{width:14px;height:14px;border-radius:50%;border:1.5px solid #94a3b8;display:block}
.f-col{width:212px}
.f-col h4{color:#fff;font-size:11.5px;font-weight:600;margin-top:8px}
.f-col ul{list-style:none;margin-top:14px}
.f-col li{font-size:11.5px;margin-bottom:13px}
.f-bottom{border-top:1px solid #1e293b;margin-top:38px;padding-top:22px;display:flex;justify-content:space-between;font-size:9.5px}
.status{display:flex;align-items:center;gap:5px}
.status:before{content:"";width:6px;height:6px;border-radius:50%;background:#22c55e}
</style>
</head>
<body>

<header class="nav">
  <div class="wrap">
    <div class="brand"><span class="brand-dot"></span>KOR GmbH</div>
    <nav class="nav-links"><span>Unternehmen</span><span>Produkte</span><span>Instandsetzung</span><span>Shop</span></nav>
    <span class="btn-contact">Kontakt aufnehmen</span>
  </div>
</header>

<section class="hero">
  <div class="hero-photo" role="img" aria-label="Lichtmaschine im Studiolicht vor dunkelgrünem Hintergrund"></div>
  <div class="wrap">
    <span class="badge"><svg width="10" height="10" viewBox="0 0 24 24" fill="none" stroke="currentColor" stroke-width="2.5"><circle cx="12" cy="8" r="6"/><path d="M8.5 13.5 7 22l5-3 5 3-1.5-8.5"/></svg>ISO 9001 ZERTIFIZIERT</span>
    <h1>Spezialist für Anlasser<br>und <span>Lichtmaschinen</span><br>seit 1992.</h1>
    <p>Ihr Partner für qualitativ hochwertige Wiederaufbereitung und Fahrzeugkomponenten. Präzision, Zuverlässigkeit und deutsche Ingenieurskunst.</p>
    <div class="hero-btns">
      <span class="btn btn-green">Zum Shop <svg width="11" height="11" viewBox="0 0 24 24" fill="none" stroke="currentColor" stroke-width="2.5"><path d="M5 12h14M13 6l6 6-6 6"/></svg></span>
      <span class="btn btn-dark">Produkte ansehen</span>
    </div>
    <div class="hero-divider"></div>
    <div class="stats">
      <div class="stat"><b>30+</b><small>JAHRE ERFAHRUNG</small></div>
      <div class="stat"><b>10k+</b><small>ARTIKEL AUF LAGER</small></div>
      <div class="stat"><b>24h</b><small>EXPRESS VERSAND</small></div>
    </div>
  </div>
</section>

<section class="cats">
  <div class="wrap">
    <div class="cats-head">
      <div>
        <h2>Unsere Produktkategorien</h2>
        <p>Hochwertige Komponenten für PKW, LKW, Landmaschinen und Industrieanwendungen.</p>
      </div>
      <span class="link-green">Alle Produkte ansehen <svg width="11" height="11" viewBox="0 0 24 24" fill="none" stroke="currentColor" stroke-width="2.5"><path d="M5 12h14M13 6l6 6-6 6"/></svg></span>
    </div>
    <div class="grid">
      <div class="card">
        <div class="icon"><svg width="18" height="18" viewBox="0 0 24 24" fill="none" stroke="currentColor" stroke-width="2"><path d="M13 2 4 14h7l-1 8 9-12h-7z"/></svg></div>
        <h3>Anlasser</h3>
        <p>Robuste Starter für alle Fahrzeugtypen. Maximale Startkraft auch unter extremen Bedingungen.</p>
        <ul class="ticks"><li><svg width="10" height="10" viewBox="0 0 24 24" fill="none" stroke="#15803d" stroke-width="3"><path d="m4 12 5 5 11-11"/></svg>Neuteile &amp; AT-Teile</li><li><svg width="10" height="10" viewBox="0 0 24 24" fill="none" stroke="#15803d" stroke-width="3"><path d="m4 12 5 5 11-11"/></svg>Prüfprotokoll inklusive</li></ul>
      </div>
      <div class="card">
        <div class="icon"><svg width="18" height="18" viewBox="0 0 24 24" fill="none" stroke="currentColor" stroke-width="2"><path d="M4 7h10M4 17h4M18 17h2"/><circle cx="17" cy="7" r="2.5"/><circle cx="12" cy="17" r="2.5"/></svg></div>
        <h3>Lichtmaschinen</h3>
        <p>Leistungsstarke Generatoren für konstante Energieversorgung. Präzise gewuchtet und getestet.</p>
        <ul class="ticks"><li><svg width="10" height="10" viewBox="0 0 24 24" fill="none" stroke="#15803d" stroke-width="3"><path d="m4 12 5 5 11-11"/></svg>Hohe Ampere-Leistung</li><li><svg width="10" height="10" viewBox="0 0 24 24" fill="none" stroke="#15803d" stroke-width="3"><path d="m4 12 5 5 11-11"/></svg>OE-Spezifikationen</li></ul>
      </div>
      <div class="card">
        <div class="icon"><svg width="18" height="18" viewBox="0 0 24 24" fill="none" stroke="currentColor" stroke-width="2"><path d="M3 8h11a3 3 0 1 0-3-3M3 12h16a3 3 0 1 1-3 3M3 16h8"/></svg></div>
        <h3>Turbolader</h3>
        <p>Effizienz und Leistung. Professionell instandgesetzte Turbolader für Diesel- und Benzinmotoren.</p>
        <ul class="ticks"><li><svg width="10" height="10" viewBox="0 0 24 24" fill="none" stroke="#15803d" stroke-width="3"><path d="m4 12 5 5 11-11"/></svg>Feingewuchtet</li><li><svg width="10" height="10" viewBox="0 0 24 24" fill="none" stroke="#15803d" stroke-width="3"><path d="m4 12 5 5 11-11"/></svg>Dichtungssätze verfügbar</li></ul>
      </div>
      <div class="card short">
        <div class="icon"><svg width="18" height="18" viewBox="0 0 24 24" fill="none" stroke="currentColor" stroke-width="2"><path d="M14 14.8V4a2 2 0 1 0-4 0v10.8a4 4 0 1 0 4 0z"/></svg></div>
        <h3>Klimakompressoren</h3>
        <p>Für ein optimales Klima. Neue und wiederaufbereitete Kompressoren höchster Güte.</p>
      </div>
      <div class="card short">
        <div class="icon"><svg width="18" height="18" viewBox="0 0 24 24" fill="none" stroke="currentColor" stroke-width="2"><rect x="3" y="7" width="16" height="10" rx="2"/><path d="M22 11v2M7 10v4M10 10v4"/></svg></div>
        <h3>Batterien</h3>
        <p>Starterbatterien und Versorgungsbatterien. Langlebig und wartungsfrei.</p>
      </div>
      <div class="card short">
        <div class="icon"><svg width="18" height="18" viewBox="0 0 24 24" fill="none" stroke="currentColor" stroke-width="2"><path d="M14.7 6.3a4 4 0 0 0 5 5L21 13l-8 8-3-3 8-8-1.3-1.3zM3 21l6-6"/></svg></div>
        <h3>Ersatzteile</h3>
        <p>Magnete, Regler, Freiläufe und weitere Kleinteile für die Instandsetzung.</p>
      </div>
    </div>
  </div>
</section>

<section class="service">
  <div class="wrap">
    <div class="service-img">
      <div class="service-frame"></div>
      <div class="service-photo" role="img" aria-label="Anker einer Lichtmaschine auf dem Prüfstand in der Werkstatt"></div>
      <div class="guarantee">
        <div class="g-ic"><svg width="14" height="14" viewBox="0 0 24 24" fill="none" stroke="currentColor" stroke-width="2.2"><path d="M12 2 4 5v6c0 5 3.5 9 8 11 4.5-2 8-6 8-11V5z"/><path d="m9 12 2 2 4-4"/></svg></div>
        <div><b>Garantie</b><small>24 Monate Gewährleistung</small></div>
      </div>
    </div>
    <div class="service-text">
      <div class="service-deco"></div>
      <div class="eyebrow">INSTANDSETZUNG</div>
      <h2>Wir bringen Ihre Teile wieder zum Laufen.</h2>
      <p class="lead">Defekte Aggregate müssen nicht immer durch Neuteile ersetzt werden. Unsere spezialisierte Werkstatt prüft, reinigt und repariert Anlasser und Lichtmaschinen nach strengen industriellen Standards.</p>
      <ul class="steps">
        <li><span class="num">1</span><div><b>Eingangsdiagnose</b><span>Detaillierte Prüfung auf unserem computergesteuerten Prüfstand.</span></div></li>
        <li><span class="num">2</span><div><b>Aufbereitung</b><span>Zerlegung, Reinigung und Austausch von Verschleißteilen.</span></div></li>
        <li><span class="num">3</span><div><b>Endkontrolle</b><span>Funktionstest mit Protokollierung der Leistungswerte.</span></div></li>
      </ul>
      <span class="link-green">Service anfragen <svg width="11" height="11" viewBox="0 0 24 24" fill="none" stroke="currentColor" stroke-width="2.5"><path d="M5 12h14M13 6l6 6-6 6"/></svg></span>
    </div>
  </div>
</section>

<section class="quality">
  <div class="wrap">
    <div class="q-left">
      <div class="eyebrow">QUALITÄT &amp; TECHNIK</div>
      <h2>Modernste Prüftechnik für maximale Zuverlässigkeit</h2>
      <p class="lead">Jedes von uns instandgesetzte Teil durchläuft einen strengen Prüfprozess auf unseren hochmodernen computergesteuerten Prüfständen. So garantieren wir, dass jedes Aggregat die volle Leistung erbringt und den höchsten industriellen Anforderungen entspricht.</p>
      <div class="q-photos">
        <div class="q-photo one" role="img" aria-label="Prüfstand mit Aggregat vor grün beleuchteter Werkstattwand"></div>
        <div class="q-photo two" role="img" aria-label="Dunkelgrüne Firmenwand mit Firmenschriftzug"></div>
      </div>
    </div>
    <div class="q-card">
      <svg class="q-shield" width="130" height="150" viewBox="0 0 24 24" fill="none" stroke="currentColor" stroke-width="1.6"><path d="M12 2 4 5v6c0 5 3.5 9 8 11 4.5-2 8-6 8-11V5z"/><path d="m9 12 2 2 4-4"/></svg>
      <h3>Der KOR Qualitäts-Standard</h3>
      <div class="q-item"><div class="q-ic"><svg width="14" height="14" viewBox="0 0 24 24" fill="none" stroke="currentColor" stroke-width="2"><circle cx="12" cy="8" r="6"/><path d="M8.5 13.5 7 22l5-3 5 3-1.5-8.5"/></svg></div><div><b>Zertifizierte Prozesse</b><span>Regelmäßige Audits und ISO 9001 Zertifizierung sichern unsere Qualitätsstandards.</span></div></div>
      <div class="q-item"><div class="q-ic"><svg width="14" height="14" viewBox="0 0 24 24" fill="none" stroke="currentColor" stroke-width="2"><rect x="3" y="4" width="18" height="12" rx="2"/><path d="M8 20h8M12 16v4"/></svg></div><div><b>Digitale Protokollierung</b><span>Jeder Test wird digital erfasst, sodass Sie ein detailliertes Leistungszertifikat erhalten.</span></div></div>
      <div class="q-item"><div class="q-ic"><svg width="14" height="14" viewBox="0 0 24 24" fill="none" stroke="currentColor" stroke-width="2"><path d="M2 7h12v9H2zM14 10h4l3 3v3h-7"/><circle cx="6" cy="18" r="2"/><circle cx="17" cy="18" r="2"/></svg></div><div><b>Logistik-Zentrum</b><span>Über 10.000 Artikel sofort verfügbar für schnellen Austausch und minimalen Stillstand.</span></div></div>
    </div>
  </div>
</section>

<section class="contact">
  <h2>Kontaktieren Sie uns</h2>
  <p class="sub">Sie haben Fragen zu einem Produkt oder benötigen technische Unterstützung? Unser Team hilft Ihnen gerne weiter.</p>
  <div class="contact-grid">
    <div class="c-info">
      <div class="c-card"><svg class="ic" width="18" height="18" viewBox="0 0 24 24" fill="none" stroke="currentColor" stroke-width="2"><path d="M12 22s7-6.5 7-12a7 7 0 0 0-14 0c0 5.5 7 12 7 12z"/><circle cx="12" cy="10" r="2.5"/></svg><b>Standort</b><span>Werkstraße 48<br>34567 Beispielfeld<br>Deutschland</span></div>
      <div class="c-card"><svg class="ic" width="18" height="18" viewBox="0 0 24 24" fill="none" stroke="currentColor" stroke-width="2"><path d="M22 16.9v3a2 2 0 0 1-2.2 2A19.8 19.8 0 0 1 2.1 4.2 2 2 0 0 1 4.1 2h3a2 2 0 0 1 2 1.7c.1 1 .4 1.9.7 2.8a2 2 0 0 1-.5 2.1L8 9.9a16 16 0 0 0 6 6l1.3-1.3a2 2 0 0 1 2.1-.4c.9.3 1.8.6 2.8.7a2 2 0 0 1 1.7 2z"/></svg><b>Telefon</b><span>+49 (0) 555 204817-0<br>Mo-Fr: 08:00 - 17:00</span></div>
      <div class="c-card"><svg class="ic" width="18" height="18" viewBox="0 0 24 24" fill="none" stroke="currentColor" stroke-width="2"><rect x="3" y="5" width="18" height="14" rx="2"/><path d="m3 7 9 6 9-6"/></svg><b>E-Mail</b><span>info@kor-gmbh.de<br>sales@kor-gmbh.de</span></div>
    </div>
    <div class="form">
      <div class="row">
        <div class="field"><label>Vorname</label><div class="input"></div></div>
        <div class="field"><label>Nachname</label><div class="input"></div></div>
      </div>
      <div class="field"><label>E-Mail Adresse</label><div class="input"></div></div>
      <div class="field"><label>Nachricht</label><div class="input textarea"></div></div>
      <div class="consent"><i></i>Ich stimme der Verarbeitung meiner Daten gemäß der <u>Datenschutzerklärung</u> zu.</div>
      <span class="btn-send">Nachricht senden</span>
    </div>
  </div>
</section>

<footer class="footer">
  <div class="wrap">
    <div class="f-top">
      <div class="f-brand">
        <div class="brand"><span class="brand-dot"></span>KOR GmbH</div>
        <p>Ihr zuverlässiger Partner für Anlasser, Lichtmaschinen und Fahrzeugelektrik. Qualität, die bewegt – seit über 30 Jahren.</p>
        <div class="socials"><i></i><i></i><i></i></div>
      </div>
      <div class="f-col"><h4>Unternehmen</h4><ul><li>Über uns</li><li>Karriere</li><li>Partner werden</li><li>Blog</li></ul></div>
      <div class="f-col"><h4>Produkte</h4><ul><li>Anlasser</li><li>Lichtmaschinen</li><li>Turbolader</li><li>Klimakompressoren</li></ul></div>
      <div class="f-col"><h4>Rechtliches</h4><ul><li>Impressum</li><li>Datenschutz</li><li>AGB</li><li>Widerruf</li></ul></div>
    </div>
    <div class="f-bottom"><span>© 2026 KOR GmbH. Alle Rechte vorbehalten. ISO 9001 Zertifiziert.</span><span class="status">Systems Operational</span></div>
  </div>
</footer>

</body>
</html>
```